Global Educational start-up needs elegant website

Hi,
I am looking for a website for a company which is serving the high-end, demanding clients in China, on educational market and working internationally. The company name is Copper Lantern Educational Services. Please find attached its logo.
We need a website consisting of seven sites:
1. What do we do? (main/basic site)
2. Programs (two subsites under this site)
a) Leadership, Entrepreneurship and Personal Development (Europe)
b) Career incubator (UK)
3. Our mission and values
4. Who are we?
5. Testimonials
6. Contact us
7. Sign for a program! (button redirecting to a form)
We would appreciate simplicity, elegance and minimalizm. It should be interactive and should meet highest expectations of the rich cusomers. On the visual materials the Chinese children aged 13-20 are preferred, in link with education, development and so on.
Time is short so we might finish the contest in a moment we find a proper choice.
Parents of rich Chinese children.
Education

```html
<!DOCTYPE html>
<html lang="en">
<head>
<meta charset="utf-8">
<title>Copper Lantern Educational Services</title>
<link href="https://fonts.googleapis.com/css2?family=Roboto:ital,wght@0,300;0,400;0,500;1,400&family=Roboto+Slab:wght@700&display=swap" rel="stylesheet">
<style>
:root{
  --green:#7aad5a;
  --green-dark:#5f9440;
  --ink:#333;
  --nav-top:#4a4a4a;
  --nav-bottom:#1f1f1f;
  --light-band:#efefef;
  --dark-band:#2a2a2a;
  --white:#fff;
}
*{box-sizing:border-box;margin:0;padding:0}
html,body{width:712px;height:1200px;overflow:hidden}
body{position:relative;background:var(--white);font-family:"Roboto",Arial,sans-serif;color:var(--ink)}
.abs{position:absolute}

/* header */
.brand{left:56px;top:21px;display:flex;align-items:center;gap:9px}
.brand-dot{width:37px;height:37px;border:2px solid #8a8a8a;border-radius:50%}
.brand-name{color:#7a7a7a;font-weight:400;line-height:1}
.brand-name .l1{display:block;font-size:15px;letter-spacing:.2px}
.brand-name .l2{display:block;font-size:5.5px;letter-spacing:2.6px;margin-top:3px;text-transform:uppercase}
.search{left:508px;top:26px;width:147px;height:28px;border:1px solid #ddd;display:flex}
.search span{flex:1;font-size:8px;color:#555;padding:8px 11px}
.search b{width:26px;background:var(--green);display:flex;align-items:center;justify-content:center}

/* nav */
.nav{left:0;top:77px;width:712px;height:38px;background:linear-gradient(var(--nav-top),var(--nav-bottom));display:flex;padding-left:52px}
.nav a{color:var(--white);text-decoration:none;font-size:8px;font-weight:400;display:flex;align-items:center;justify-content:center;border-right:1px solid #555;height:100%}
.nav a.active{background:var(--green);border:none}
.nav a:last-child{border:none}

/* hero */
.hero{left:51px;top:115px;width:608px;height:287px;
  background:
    radial-gradient(ellipse 120px 150px at 82% 60%,rgba(245,243,240,.95),transparent 70%),
    radial-gradient(ellipse 70px 90px at 80% 18%,rgba(196,140,100,.9),transparent 75%),
    radial-gradient(ellipse 80px 120px at 75% 35%,rgba(150,90,60,.55),transparent 75%),
    radial-gradient(ellipse 90px 140px at 43% 75%,rgba(30,30,34,.55),transparent 70%),
    radial-gradient(ellipse 80px 130px at 12% 70%,rgba(60,60,66,.5),transparent 70%),
    linear-gradient(180deg,#c9c3bb 0%,#a9a39b 55%,#8e8982 100%)}
.hero-title{left:86px;top:226px;font-family:"Roboto Slab",Georgia,serif;font-weight:700;font-size:14.5px;line-height:27px;color:var(--white);text-shadow:0 1px 3px rgba(0,0,0,.7)}
.btn-green{left:86px;top:285px;width:86px;height:28px;background:linear-gradient(#86ba65,var(--green-dark));color:var(--white);font-size:10px;font-weight:500;display:flex;align-items:center;justify-content:center;border-radius:2px}
.dots{left:528px;top:392px;display:flex;gap:8px}
.dots i{width:27px;height:2px;background:var(--white)}
.dots i:first-child{background:var(--green)}
.shadow{left:120px;top:402px;width:470px;height:16px;background:radial-gradient(ellipse at top,rgba(0,0,0,.18),transparent 70%)}

/* services */
.section-title{left:0;width:712px;text-align:center;font-size:14px;font-weight:500;color:#333}
.card{top:455px;width:197px;height:131px}
.card-photo{width:100%;height:100%}
.card-cap{position:absolute;left:0;bottom:0;width:100%;height:30px;background:rgba(50,50,50,.72);color:var(--white);font-size:10px;font-weight:400;padding:9px 15px}
.card-shadow{position:absolute;left:15px;bottom:-14px;width:170px;height:12px;background:radial-gradient(ellipse at top,rgba(0,0,0,.18),transparent 70%)}

/* welcome */
.welcome-band{left:0;top:610px;width:712px;height:213px;background:var(--green)}
.welcome-title{left:55px;top:641px;color:var(--white);font-size:14px;font-weight:500}
.welcome-copy{left:56px;top:665px;width:284px;font-size:7.9px;font-weight:300;line-height:16.5px;color:var(--white)}
.btn-dark{left:57px;top:774px;width:74px;height:23px;background:linear-gradient(#444,#1e1e1e);color:var(--white);font-size:9px;display:flex;align-items:center;justify-content:center;border-radius:3px}
.video-frame{left:369px;top:630px;width:288px;height:175px;background:var(--white);padding:6px;box-shadow:0 1px 3px rgba(0,0,0,.25)}
.video{position:relative;width:100%;height:100%;border-radius:3px;overflow:hidden;
  background:
    radial-gradient(ellipse 40px 60px at 20% 55%,rgba(230,215,200,.8),transparent 70%),
    radial-gradient(ellipse 40px 60px at 60% 60%,rgba(70,110,170,.7),transparent 70%),
    radial-gradient(ellipse 40px 60px at 85% 60%,rgba(140,175,205,.8),transparent 70%),
    radial-gradient(ellipse 35px 50px at 40% 65%,rgba(60,60,70,.7),transparent 70%),
    linear-gradient(180deg,#d9d3cc 0%,#b59a84 40%,#7e8794 100%)}
.play{position:absolute;left:120px;top:56px;width:32px;height:32px;border-radius:50%;background:rgba(40,40,40,.6);display:flex;align-items:center;justify-content:center}
.controls{position:absolute;left:0;bottom:0;width:100%;height:22px;background:#1b1b1b;display:flex;align-items:center;padding:0 7px;gap:6px;font-size:6px;color:#ddd}
.track{flex:1;height:2px;background:#666;position:relative}
.track i{position:absolute;left:0;top:0;width:35%;height:2px;background:#e03a3a}

/* testimonials */
.quote{top:888px;width:200px;height:100px}
.avatar{position:absolute;left:0;top:0;width:56px;height:56px;border-radius:50%}
.quote-text{position:absolute;left:81px;top:11px;width:100px;font-size:7px;font-style:italic;line-height:13.5px;color:#555}
.qm{position:absolute;font-family:Georgia,serif;font-size:15px;color:#aaa}
.q-name{position:absolute;left:79px;top:68px;font-size:7.5px;color:var(--green);text-transform:uppercase}
.q-role{position:absolute;left:79px;top:81px;font-size:7px;font-style:italic;color:var(--green)}

/* footer */
.foot{left:0;top:1003px;width:712px;height:115px;background:var(--light-band)}
.fcol{top:1026px}
.fcol h3{font-size:9.5px;font-weight:400;color:var(--green);margin-bottom:9px}
.fcol li{list-style:none;font-size:9px;color:#444;line-height:16.7px}
.base{left:0;top:1118px;width:712px;height:82px;background:var(--dark-band)}
.legal{left:57px;top:1147px;font-size:8px;font-weight:400;color:var(--white)}
.copy{left:57px;top:1164px;font-size:7px;font-weight:400;color:var(--white)}
.social{left:564px;top:1150px;display:flex;gap:6px}
.social i{width:19px;height:19px;border-radius:2px}
</style>
</head>
<body>

<header>
  <div class="abs brand">
    <div class="brand-dot"></div>
    <div class="brand-name"><span class="l1">COPPER LANTERN</span><span class="l2">Educational Services</span></div>
  </div>
  <div class="abs search"><span>Search</span><b>
    <svg width="11" height="11" viewBox="0 0 11 11"><circle cx="4.5" cy="4.5" r="3.2" fill="none" stroke="#fff" stroke-width="1.4"/><line x1="7" y1="7" x2="10" y2="10" stroke="#fff" stroke-width="1.6"/></svg></b></div>
</header>

<nav class="abs nav">
  <a class="active" style="width:94px">WHAT DO WE DO?</a>
  <a style="width:82px">PROGRAMS</a>
  <a style="width:136px">OUR MISSION AND VALUES</a>
  <a style="width:90px">WHO ARE WE?</a>
  <a style="width:86px">CONTACT US</a>
  <a style="width:120px">SIGN FOR A PROGRAM!</a>
</nav>

<section>
  <div class="abs hero" role="img" aria-label="Smiling young professional giving a thumbs up in front of a blurred business crowd shaking hands"></div>
  <h1 class="abs hero-title">LOREM IPSUM IS SIMPLY DUMMY TEXT OF THE<br>PRINTING AND TYPESETTING INDUSTRY</h1>
  <div class="abs btn-green">VIEW MORE</div>
  <div class="abs dots"><i></i><i></i><i></i><i></i></div>
  <div class="abs shadow"></div>
</section>

<section>
  <h2 class="abs section-title" style="top:425px">SERVICES</h2>
  <div class="abs card" style="left:54px">
    <div class="card-photo" role="img" aria-label="Students studying together at classroom desks" style="background:radial-gradient(ellipse 50px 40px at 30% 40%,rgba(240,235,228,.8),transparent 70%),radial-gradient(ellipse 60px 40px at 75% 70%,rgba(200,140,80,.7),transparent 70%),linear-gradient(160deg,#cdb796 0%,#a9865f 50%,#6f6458 100%)"></div>
    <div class="card-cap">WHAT DO WE DO</div><div class="card-shadow"></div></div>
  <div class="abs card" style="left:257px">
    <div class="card-photo" role="img" aria-label="Young students writing in notebooks" style="background:radial-gradient(ellipse 60px 50px at 45% 40%,rgba(205,160,120,.8),transparent 70%),radial-gradient(ellipse 50px 60px at 85% 50%,rgba(230,200,140,.8),transparent 70%),linear-gradient(170deg,#cfdcc2 0%,#e4d6c4 50%,#f3efe9 100%)"></div>
    <div class="card-cap">PROGRAMS</div><div class="card-shadow"></div></div>
  <div class="abs card" style="left:461px">
    <div class="card-photo" role="img" aria-label="Group of smiling students in front of a chalkboard" style="background:radial-gradient(ellipse 50px 50px at 30% 45%,rgba(210,160,130,.8),transparent 70%),radial-gradient(ellipse 50px 60px at 70% 55%,rgba(235,215,180,.8),transparent 70%),linear-gradient(170deg,#6f8d7c 0%,#b99b84 50%,#e8e3dd 100%)"></div>
    <div class="card-cap">OUR MISSION AND VALUES</div><div class="card-shadow"></div></div>
</section>

<section>
  <div class="abs welcome-band"></div>
  <h2 class="abs welcome-title">WELCOME TO COPPER LANTERN</h2>
  <p class="abs welcome-copy">Lorem Ipsum has been the industry's standard dummy text ever since the 1500s, when an unknown printer took a galley of type and scrambled it to make a type specimen book. It has survived not only five centuries, but also the leap into electronic typesetting, remaining essentially unchanged. It was popularised in the 1960s with the release of Setwell sheets containing like Quillpress Layout including versions of Lorem Ipsum</p>
  <div class="abs btn-dark">Read More</div>
  <div class="abs video-frame">
    <div class="video" role="img" aria-label="Video still of a cheerful group of students giving thumbs up">
      <div class="play"><svg width="12" height="14" viewBox="0 0 12 14"><path d="M1 1l10 6-10 6z" fill="#fff"/></svg></div>
      <div class="controls">
        <svg width="9" height="9" viewBox="0 0 9 9"><circle cx="4.5" cy="4.5" r="3.6" fill="none" stroke="#fff"/><path d="M3.5 2.8l2.6 1.7-2.6 1.7z" fill="#fff"/></svg>
        <svg width="20" height="7" viewBox="0 0 20 7"><path d="M0 2h2l2-2v7l-2-2H0z" fill="#e03a3a"/><rect x="7" y="1" width="13" height="5" fill="#e03a3a" opacity=".8"/></svg>
        <div class="track"><i></i></div>
        <span>01:30 / 04:55</span>
        <svg width="8" height="7" viewBox="0 0 8 7"><rect x=".5" y=".5" width="7" height="6" fill="none" stroke="#fff"/></svg>
        <svg width="8" height="8" viewBox="0 0 8 8"><circle cx="4" cy="4" r="2.6" fill="none" stroke="#fff" stroke-width="1.6"/></svg>
      </div>
    </div>
  </div>
</section>

<section>
  <h2 class="abs section-title" style="top:847px">TESTIMONIALS</h2>
  <div class="abs quote" style="left:50px">
    <div class="avatar" role="img" aria-label="Portrait of a smiling man in a shirt and tie" style="background:radial-gradient(circle at 50% 38%,#d9b49a 0 30%,transparent 32%),linear-gradient(180deg,#f2f2f2 0 60%,#8fb3d6 60%)"></div>
    <span class="qm" style="left:65px;top:-4px">&ldquo;</span><p class="quote-text">Lorem Ipsum is simply dummy text of the printing and typeset-ting industry.</p><span class="qm" style="left:180px;top:38px">&rdquo;</span><div class="q-name">Morgan Ellis</div><div class="q-role">Marketing Executive</div></div>
  <div class="abs quote" style="left:260px">
    <div class="avatar" role="img" aria-label="Portrait of a smiling woman" style="background:radial-gradient(circle at 50% 40%,#e2c0a6 0 26%,#8a5c3c 28% 42%,transparent 44%),linear-gradient(180deg,#f4f4f4 0 65%,#e6e1dc 65%)"></div>
    <span class="qm" style="left:65px;top:-4px">&ldquo;</span><p class="quote-text">Lorem Ipsum is simply dummy text of the printing and typeset-ting industry.</p><span class="qm" style="left:180px;top:38px">&rdquo;</span><div class="q-name">Morgan Ellis</div><div class="q-role">Marketing Executive</div></div>
  <div class="abs quote" style="left:465px">
    <div class="avatar" role="img" aria-label="Portrait of a smiling man" style="background:radial-gradient(circle at 50% 40%,#c99a7c 0 28%,transparent 30%),linear-gradient(180deg,#eeeeee 0 62%,#6d7580 62%)"></div>
    <span class="qm" style="left:65px;top:-4px">&ldquo;</span><p class="quote-text">Lorem Ipsum is simply dummy text of the printing and typeset-ting industry.</p><span class="qm" style="left:180px;top:38px">&rdquo;</span><div class="q-name">Morgan Ellis</div><div class="q-role">Marketing Executive</div></div>
</section>

<footer>
  <div class="abs foot"></div>
  <div class="abs fcol" style="left:58px"><h3>COMPANY</h3><ul><li>About us</li><li>Services</li><li>Presentation</li></ul></div>
  <div class="abs fcol" style="left:174px"><h3>SPECIALISTS</h3><ul><li>Commercial</li><li>Residential</li><li>Luxury</li></ul></div>
  <div class="abs fcol" style="left:287px"><h3>ADVICE</h3><ul><li>FAQs</li><li>Support</li></ul></div>
  <div class="abs fcol" style="left:382px"><h3>AGENCIES</h3><ul><li>Sign Up</li><li>Forums</li><li>Promotions</li></ul></div>
  <div class="abs fcol" style="left:487px"><h3>CONTACT US</h3><ul><li>14 Alder Quay, Harbourton, HT3 7QL</li><li>Phone: +1 800 555 0142</li><li>E-mail: hello@copperlantern.org</li></ul></div>
  <div class="abs base"></div>
  <div class="abs legal">Privacy Policy &nbsp;|&nbsp; Terms of Use &nbsp;|&nbsp; About Us &nbsp;|&nbsp; Sitemap</div>
  <div class="abs copy">Copyright © 2014 All Rights</div>
  <div class="abs social"><i style="background:#2fa8e0"></i><i style="background:#d6322b"></i><i style="background:#3b5a9a"></i><i style="background:#1a77b5"></i></div>
</footer>

</body>
</html>
```